Billboard Design for Modern Dispensary

Hello!
We need a eye-catching 12' x 24' billboard designed for a very successful, modern cannabis dispensary on the Oregon coast, United States. Because of rules, we cannot have any marijuana leafs or other cannabis related images (flower, joints, smoke, etc). We can use the words "Shop" or "Dispensary" - we cannot use the words "cannabis", "marijuana".

Some ideas we had are 3 words stacked on left or center of billboard - maybe across bottom we have horizontal logo and the following words - “North of Harbor in Gull Cove”
Another idea is to have a small bubble in bottom/top corner with image of our dog (face only) - with some words around it - like "BONUS Shop Dog" or "Cute Shop Dog" or "Best Shop Dog" or "Friendly Staff"

here's some 3 word examples:
ENJOY
YOUR
TRIP

or

FEEL
GOOD
JUST
AHEAD

or

GOOD
VIBES
ONLY

or

GOOD
TIMES
CHILL
VIBES

I have attached our logo. I have also included a stacked logo version (vertical, not horizontal). the formats are .EPS and .PDF - the logos were created in Affinity Design 2.x.

Our website is coralnook.net if you want to see more images, etc about our dispensary.

Artwork Requirements:
The billboard is 12' tall x 25' wide
The artwork needs to be 1”=1’ @ 300dpi
Please add 6” of bleed all around so your total artwork is 13”x26”
Final deliverable should be .Ai file.

Font styles to use
Sans Serif

Colors
0054AA
0677BA
7BADD7
CADEEF
E8F1F8

Requirements
Nice to have
• See the project description - we included some ideas to consider.
Should not have
• No cannabis images, like flower, cannabis leaves, paraphenlia, cartridges, joints, etc.

```html
<!DOCTYPE html>
<html lang="en">
<head>
<meta charset="utf-8">
<title>Coral Nook Billboard</title>
<link rel="stylesheet" href="https://fonts.googleapis.com/css2?family=Archivo:wght@400;800;900&family=Oswald:wght@700&display=swap">
<style>
  :root {
    --backdrop: #474a4d;
    --sky-blue: #449ad8;
    --ink: #000000;
    --paper: #ffffff;
    --paper-shade: #dfe5ea;
    --soft-shadow: #e3e6ea;
  }
  * { margin: 0; padding: 0; box-sizing: border-box; }
  html, body {
    width: 968px;
    height: 1200px;
    overflow: hidden;
    background: var(--backdrop);
  }
  .canvas {
    position: relative;
    width: 968px;
    height: 1200px;
  }
  .billboard {
    position: absolute;
    left: 34px;
    top: 375px;
    width: 900px;
    height: 450px;
    overflow: hidden;
    background: var(--paper);
  }
  .stone-texture {
    position: absolute;
    inset: 0 0 186px 0;
    background:
      radial-gradient(ellipse at 25% 40%, var(--paper-shade) 0%, rgba(223,229,234,0) 55%),
      radial-gradient(ellipse at 70% 60%, #eef1f4 0%, rgba(238,241,244,0) 60%),
      linear-gradient(180deg, #f7f8f9 0%, #eceff2 100%);
  }
  .brand {
    position: absolute;
    left: 64px;
    top: 33px;
    width: 350px;
    text-align: center;
  }
  .brand-dot {
    display: block;
    width: 122px;
    height: 122px;
    margin: 0 auto 10px;
    border-radius: 50%;
    border: 12px solid var(--sky-blue);
    background: var(--paper);
  }
  .brand-name {
    font-family: "Archivo", sans-serif;
    font-weight: 400;
    font-size: 50px;
    line-height: 1;
    white-space: nowrap;
    color: var(--sky-blue);
    text-transform: uppercase;
  }
  .location {
    position: absolute;
    left: 470px;
    top: 46px;
    font-family: "Archivo", sans-serif;
    font-weight: 900;
    font-size: 62px;
    line-height: 68px;
    white-space: nowrap;
    color: var(--sky-blue);
    text-shadow: 3px 3px 0 var(--soft-shadow);
    text-transform: uppercase;
  }
  .tagline-band {
    position: absolute;
    left: 0;
    top: 264px;
    width: 100%;
    height: 102px;
    background: var(--sky-blue);
    display: flex;
    align-items: center;
    justify-content: center;
  }
  .tagline {
    font-family: "Oswald", sans-serif;
    font-weight: 700;
    font-size: 78px;
    line-height: 1;
    white-space: nowrap;
    color: var(--paper);
    text-shadow: 4px 4px 0 var(--ink);
    text-transform: uppercase;
  }
  .action-band {
    position: absolute;
    left: 0;
    top: 366px;
    width: 100%;
    height: 84px;
    background: var(--ink);
  }
  .shop-tag {
    position: absolute;
    left: 128px;
    top: 12px;
    width: 304px;
    height: 54px;
    background: var(--paper);
    transform: rotate(-4deg);
    clip-path: polygon(4% 0, 100% 0, 100% 100%, 0 100%);
    display: flex;
    align-items: center;
    justify-content: center;
    font-family: "Archivo", sans-serif;
    font-weight: 800;
    font-size: 34px;
    white-space: nowrap;
    color: var(--sky-blue);
    text-transform: uppercase;
  }
  .web-address {
    position: absolute;
    left: 470px;
    top: 23px;
    font-family: "Archivo", sans-serif;
    font-weight: 400;
    font-size: 36px;
    line-height: 1;
    white-space: nowrap;
    color: var(--sky-blue);
    text-transform: uppercase;
  }
</style>
</head>
<body>
<main class="canvas">
  <section class="billboard">
    <div class="stone-texture" role="img" aria-label="Soft pale grey marble texture background"></div>

    <div class="brand">
      <span class="brand-dot"></span>
      <div class="brand-name">Coral Nook</div>
    </div>

    <h1 class="location">North of<br>Harbor in<br>Gull Cove</h1>

    <div class="tagline-band">
      <p class="tagline">Feel Good Just Ahead</p>
    </div>

    <div class="action-band">
      <div class="shop-tag">Shop Today!!</div>
      <p class="web-address">coralnook.net</p>
    </div>
  </section>
</main>
</body>
</html>
```